Healthy Supplement featuring Moringa products

Need 3 business card options for our reps to order from Cardloom. Our reps will be ordering from Cardloom once we upload them. Attached is our current designs to show what info needs to be on the cards. Our website is www.tkvitality.com
The business cards will be a template for our reps to order from. Most of our reps are Asian & Hispanic. Please look at our website so you can see who we are to get the look and feel what we need.
Target Market(s)
Adults 30 on up. Health oriented people.
Industry/Entity Type
Health And Wellness
Contact Information for Business Card
Name
Title
Phone
Logo
www.tkvitality.com/my/username
Font styles to use
Requirements
Must have
- Please match our website look and colors. A moringa leaf is nice, but am open to something different.
Nice to have
- Healthy looking and warm, not super cold or too modern.
Should not have
- No harsh colors please.

```html
<!DOCTYPE html>
<html lang="en">
<head>
<meta charset="utf-8">
<title>TK Vitality – Business Card</title>
<link rel="stylesheet" href="https://fonts.googleapis.com/css2?family=Lora:wght@400;700&display=swap">
<style>
  :root {
    --backdrop: #ebe6de;
    --card-white: #ffffff;
    --leaf-green: #6aaa3e;
    --leaf-green-light: #8cc04f;
    --leaf-green-deep: #5d9e36;
    --text-grey: #555555;
    --rule-grey: #666666;
    --faint-leaf: #f1f4ee;
  }
  * { margin: 0; padding: 0; box-sizing: border-box; }
  html, body {
    width: 900px; height: 1200px; overflow: hidden;
    background: var(--backdrop);
  }
  .canvas { position: relative; width: 900px; height: 1200px; }
  .card {
    position: absolute; left: 86px; width: 736px; height: 430px;
    border-radius: 22px; overflow: hidden;
    box-shadow: 0 6px 14px rgba(0,0,0,0.25);
  }
  .card-front { top: 137px; background: var(--card-white); }
  .card-back {
    top: 633px;
    background: linear-gradient(120deg, var(--leaf-green-deep) 0%, var(--leaf-green) 45%, var(--leaf-green-light) 75%, var(--leaf-green) 100%);
  }
  .brand-name {
    font-family: "Lora", serif; font-weight: 400;
    letter-spacing: 1px; white-space: nowrap;
  }
  .front-brand {
    position: absolute; right: 54px; top: 86px;
    font-size: 36px; color: var(--leaf-green);
  }
  .faint-leaf-area {
    position: absolute; right: 50px; top: 205px; width: 200px; height: 200px;
    background: radial-gradient(ellipse at center, var(--faint-leaf) 0%, rgba(241,244,238,0) 70%);
  }
  .rep-name {
    position: absolute; left: 53px; top: 236px;
    font-family: "Lora", serif; font-weight: 700; font-size: 30px;
    color: var(--leaf-green);
  }
  .contact-list {
    position: absolute; left: 53px; top: 300px;
    border-left: 3px solid var(--rule-grey);
    padding-left: 20px; list-style: none;
  }
  .contact-item {
    display: flex; align-items: center; gap: 10px;
    font-family: "Lora", serif; font-size: 17px; color: var(--text-grey);
    height: 28.5px;
  }
  .contact-icon { width: 13px; height: 13px; fill: var(--leaf-green); }
  .front-band {
    position: absolute; left: 0; bottom: 0; width: 100%; height: 24px;
    background: var(--leaf-green);
  }
  .band-gap {
    position: absolute; left: 463px; bottom: 0; width: 6px; height: 24px;
    background: var(--card-white);
  }
  .back-waves { position: absolute; inset: 0; }
  .back-brand {
    position: absolute; left: 0; right: 0; top: 175px; text-align: center;
    font-size: 64px; color: var(--card-white);
  }
</style>
</head>
<body>
<main class="canvas">
  <section class="card card-front" aria-label="Card front">
    <div class="brand-name front-brand">TK Vitality</div>
    <div class="faint-leaf-area" role="img" aria-label="Faint moringa leaf branch decoration"></div>
    <h1 class="rep-name">Lena Marquez</h1>
    <ul class="contact-list">
      <li class="contact-item">
        <svg class="contact-icon" viewBox="0 0 24 24"><path d="M6.6 10.8a15 15 0 0 0 6.6 6.6l2.2-2.2a1 1 0 0 1 1-.25 11.4 11.4 0 0 0 3.6.57 1 1 0 0 1 1 1V20a1 1 0 0 1-1 1A17 17 0 0 1 3 4a1 1 0 0 1 1-1h3.5a1 1 0 0 1 1 1c0 1.25.2 2.45.57 3.57a1 1 0 0 1-.25 1z"/></svg>
        000-000-0000
      </li>
      <li class="contact-item">
        <svg class="contact-icon" viewBox="0 0 24 24"><path d="M2 5h20v2l-10 6L2 7z M2 9l10 6 10-6v10H2z"/></svg>
        lena.marquez@tkvitality.com
      </li>
      <li class="contact-item">
        <svg class="contact-icon" viewBox="0 0 24 24"><circle cx="12" cy="12" r="10" fill="none" stroke="currentColor" style="stroke:var(--leaf-green)" stroke-width="2"/><path d="M2 12h20M12 2c3 3 3 17 0 20M12 2c-3 3-3 17 0 20" fill="none" style="stroke:var(--leaf-green)" stroke-width="2"/></svg>
        www.tkvitality.com/my/username
      </li>
    </ul>
    <div class="front-band"></div>
    <div class="band-gap"></div>
  </section>

  <section class="card card-back" aria-label="Card back">
    <svg class="back-waves" viewBox="0 0 736 430" preserveAspectRatio="none" aria-hidden="true">
      <path d="M0 90 C200 60 380 120 736 210 L736 0 L0 0 Z" fill="#ffffff" opacity="0.05"/>
      <path d="M0 215 C220 200 420 250 736 330 L736 430 L0 430 Z" fill="#ffffff" opacity="0.06"/>
      <path d="M520 0 C600 120 560 300 736 430 L736 0 Z" fill="#ffffff" opacity="0.05"/>
    </svg>
    <div class="brand-name back-brand">TK Vitality</div>
  </section>
</main>
</body>
</html>
```